Billboard Design for Modern Dispensary

Hello!
We need a eye-catching 12' x 24' billboard designed for a very successful, modern cannabis dispensary on the Oregon coast, United States. Because of rules, we cannot have any marijuana leafs or other cannabis related images (flower, joints, smoke, etc). We can use the words "Shop" or "Dispensary" - we cannot use the words "cannabis", "marijuana".

Some ideas we had are 3 words stacked on left or center of billboard - maybe across bottom we have horizontal logo and the following words - “South of bridge in Marlow Cove”
Another idea is to have a small bubble in bottom/top corner with image of our dog (face only) - with some words around it - like "BONUS Shop Dog" or "Cute Shop Dog" or "Best Shop Dog" or "Friendly Staff"

here's some 3 word examples:
ENJOY
YOUR
TRIP

or

FEEL
GOOD
JUST
AHEAD

or

GOOD
VIBES
ONLY

or

GOOD
TIMES
CHILL
VIBES

I have attached our logo. I have also included a stacked logo version (vertical, not horizontal). the formats are .EPS and .PDF - the logos were created in Affinity Design 2.x.

Our website is lunarwharf.com if you want to see more images, etc about our dispensary.

Artwork Requirements:
The billboard is 12' tall x 25' wide
The artwork needs to be 1”=1’ @ 300dpi
Please add 6” of bleed all around so your total artwork is 13”x26”
Final deliverable should be .Ai file.

Font styles to use
Sans Serif

Colors
0054AA
0677BA
7BADD7
CADEEF
E8F1F8

Requirements
Nice to have
• See the project description - we included some ideas to consider.
Should not have
• No cannabis images, like flower, cannabis leaves, paraphenlia, cartridges, joints, etc.

```html
<!DOCTYPE html>
<html lang="en">
<head>
<meta charset="utf-8">
<title>Lunar Wharf — Best Shop Period</title>
<link href="https://fonts.googleapis.com/css2?family=Black+Ops+One&family=Montserrat:wght@300;700;800&display=swap" rel="stylesheet">
<style>
  :root {
    --teal: #0e3f46;
    --teal-deep: #0a2f34;
    --cream: #f4ecda;
    --white: #ffffff;
    --coat-light: #e9c48a;
    --coat-dark: #c8914d;
  }
  * { margin: 0; padding: 0; box-sizing: border-box; }
  html, body { width: 1200px; height: 600px; overflow: hidden; }
  body { background: var(--teal); }
  .billboard {
    position: relative;
    width: 1200px;
    height: 600px;
    background: var(--teal);
    overflow: hidden;
    font-family: "Montserrat", sans-serif;
  }

  /* Stacked headline: each word is one text run so shadows sit beneath every letter */
  .headline {
    position: absolute;
    left: 112px;
    top: 72px;
    font-family: "Black Ops One", sans-serif;
    font-weight: 400;
    font-size: 126px;
    line-height: 130px;
    letter-spacing: 10px;
    color: var(--cream);
    white-space: nowrap;
    text-shadow:
      -2px 3px 0 var(--teal-deep),
      -4px 6px 0 var(--teal-deep),
      -6px 9px 0 var(--teal-deep),
      -8px 12px 0 var(--teal-deep),
      -10px 15px 0 var(--teal-deep),
      -12px 18px 0 var(--teal-deep),
      -13px 21px 0 var(--teal-deep);
  }
  .headline-word {
    display: block;
    height: 149px;
  }

  /* Shop dog badge */
  .dog-badge {
    position: absolute;
    left: 831px;
    top: 52px;
    width: 286px;
    height: 286px;
  }
  .dog-badge svg { display: block; }
  .badge-label {
    font-family: "Montserrat", sans-serif;
    font-weight: 800;
    font-size: 27px;
    letter-spacing: 1px;
    fill: var(--teal);
  }

  /* Brand lockup */
  .brand {
    position: absolute;
    left: 766px;
    top: 406px;
    display: flex;
    align-items: center;
    gap: 10px;
  }
  .brand-mark {
    width: 96px;
    height: 96px;
    border: 4px solid var(--white);
    border-radius: 50%;
    flex: none;
  }
  .brand-text { display: flex; flex-direction: column; align-items: center; }
  .brand-name {
    font-family: "Montserrat", sans-serif;
    font-weight: 300;
    font-size: 36px;
    line-height: 40px;
    color: var(--white);
    letter-spacing: -0.5px;
    white-space: nowrap;
  }
  .brand-place {
    display: flex;
    align-items: center;
    gap: 10px;
    margin-top: 6px;
    font-family: "Montserrat", sans-serif;
    font-weight: 300;
    font-size: 11px;
    letter-spacing: 6px;
    color: var(--white);
    white-space: nowrap;
  }
  .brand-rule { width: 40px; height: 1px; background: var(--white); }

  .tagline {
    position: absolute;
    left: 717px;
    top: 512px;
    font-family: "Montserrat", sans-serif;
    font-weight: 700;
    font-size: 25px;
    color: var(--white);
    white-space: nowrap;
  }
</style>
</head>
<body>
<main class="billboard">

  <h1 class="headline">
    <span class="headline-word">BEST</span>
    <span class="headline-word">SHOP</span>
    <span class="headline-word">PERIOD</span>
  </h1>

  <div class="dog-badge">
    <svg width="286" height="286" viewBox="0 0 286 286">
      <defs>
        <radialGradient id="coat" cx="50%" cy="55%" r="45%">
          <stop offset="0%" stop-color="#e9c48a"/>
          <stop offset="100%" stop-color="#c8914d"/>
        </radialGradient>
        <path id="badgeArc" d="M 42 143 A 101 101 0 0 1 244 143"/>
      </defs>
      <circle cx="143" cy="143" r="143" fill="#f4ecda"/>
      <ellipse cx="146" cy="165" rx="92" ry="112" fill="url(#coat)" role="img" aria-label="Photo of the shop dog, a smiling golden doodle"/>
      <text class="badge-label"><textPath href="#badgeArc" startOffset="50%" text-anchor="middle">CUTE SHOP DOG</textPath></text>
    </svg>
  </div>

  <div class="brand">
    <span class="brand-mark" aria-hidden="true"></span>
    <div class="brand-text">
      <span class="brand-name">LUNAR WHARF</span>
      <span class="brand-place"><span class="brand-rule"></span>MARLOW COVE<span class="brand-rule"></span></span>
    </div>
  </div>

  <p class="tagline">South of bridge in Marlow Cove</p>

</main>
</body>
</html>
```